Test and Tag business card design

We are an appliance test and tag company in Brisbane Australia requiring a business card design.
I don't have a logo.
Card front: Matte black background with white font.
Card back: White background with black font colour
Examples are attached
Minimalist design
Reason: Looking for more designs with an extreme minimal feel
Industry/Entity Type
Appliance
Contact Information for Business Card
Business name: Harbor Check and Label
Description: Onsite Electrical Testing and Tagging
Licence No. 41853
Name: Greg Pellow
Mobile: 0418 526 937
Email: greg@harborcheckandlabel.com.au
Web: harborcheckandlabel.com.au
Logo Text
Harbor Check and Label
Look and feel

```html
<!DOCTYPE html>
<html lang="en">
<head>
<meta charset="utf-8">
<title>Harbor Check and Label – Business Card Front</title>
<link rel="stylesheet" href="https://fonts.googleapis.com/css2?family=Arimo:wght@400&family=Noto+Sans:wght@400&display=swap">
<style>
  :root {
    --matte-black: #111111;
    --ink-white: #ffffff;
    --label-white: #bdbdbd;
  }
  * { margin: 0; padding: 0; box-sizing: border-box; }
  html, body {
    width: 1200px;
    height: 693px;
    overflow: hidden;
    background: var(--matte-black);
  }
  .card-front {
    position: relative;
    width: 1200px;
    height: 693px;
    overflow: hidden;
    background: var(--matte-black);
    color: var(--ink-white);
    font-family: "Noto Sans", Verdana, sans-serif;
    font-weight: 400;
    line-height: 1;
    white-space: nowrap;
  }
  .card-text { position: absolute; }
  .label { color: var(--label-white); }
  .value { color: var(--ink-white); }

  .business-name {
    left: 0;
    right: 0;
    top: 52px;
    text-align: center;
    font-family: "Arimo", Arial, sans-serif;
    font-weight: 400;
    font-size: 94px;
    letter-spacing: 0.5px;
  }
  .tagline {
    left: 68px;
    top: 186px;
    font-size: 50px;
  }
  .holder-name { left: 94px; top: 298px; }
  .holder-name .label { font-size: 36px; }
  .holder-name .value { font-size: 56px; margin-left: 12px; }

  .licence { left: 706px; top: 304px; }
  .licence .label { font-size: 36px; }
  .licence .value { font-size: 48px; margin-left: 6px; }

  .mobile { left: 653px; top: 453px; }
  .mobile .label { font-size: 38px; }
  .mobile .value { font-size: 52px; margin-left: 8px; }

  .email { left: 8px; top: 556px; font-family: "Arimo", Arial, sans-serif; }
  .email .label { font-size: 38px; }
  .email .value { font-size: 40px; margin-left: 6px; }

  .web { right: 20px; top: 632px; font-family: "Arimo", Arial, sans-serif; }
  .web .label { font-size: 38px; }
  .web .value { font-size: 40px; margin-left: 6px; }
</style>
</head>
<body>
  <main class="card-front">
    <h1 class="card-text business-name">Harbor Check and Label</h1>
    <p class="card-text tagline">Onsite Electrical Testing and Tagging</p>

    <p class="card-text holder-name"><span class="label">Name:</span><span class="value"> Greg Pellow</span></p>
    <p class="card-text licence"><span class="label">Licence No.</span><span class="value"> 41853</span></p>
    <p class="card-text mobile"><span class="label">Mobile:</span><span class="value"> 0418 526 937</span></p>
    <p class="card-text email"><span class="label">Email:</span><span class="value"> greg@harborcheckandlabel.com.au</span></p>
    <p class="card-text web"><span class="label">Web:</span><span class="value"> harborcheckandlabel.com.au</span></p>
  </main>
</body>
</html>
```